IT Services Business Card Design

We require a business card design for an IT services company called RT Code Transit.

We specialize in taking an organisations software and readying it for deployment to new environments (e.g. Nex 3 to Nex 5). This process is termed application packaging. This is not the same as putting things in boxes but I am happy to use boxes as a pun icon ;-) This is our second step in branding, we currently have a new logo and our poor excuse of a website is next to be updated but it contains information on who we are and what we cover at rtcodetransit.example

We are looking for a fun, modern but stylish and professional looking design.

I have attached the logo in multiple formats including vector formats (and the fonts that created the logo if required)
Updates

Thanks to all the designers so far, some great designs in there.  I will be selecting a card design on the deadline date. 

However, there is still time to submit some more designs.  The majority of the ones I have so far are typical simplistic designs that we have all seen before and I have enough of those to choose from now.  If you wish to submit any more designs, please submit somthing unusual to grab our attention.

Target Market(s)

Project executives of large organisations looking for Nexora migrations

Industry/Entity Type

Software

Requirements
Must have
• Want to show company name, contact name, title, main number, contact number, fax number, email address and website address. I do not want to show the address.
Must use the attached logo, retaining the colours in them.

This has to be a double-sided design. I will be using pelby.example and will be selecting their rounded corner business card design.

Their templates and design requirements (sizing etc.) can be found here: http://uk.pelby.example/help/faq/templates-and-guidelines.html

Happy for company name or website to be on either side of the card.

This design has to be original and not used before for another company

Would like to style it around the business colours in the logo
Nice to have
• Pelby.example has an option for multiple card designs to appear on the back. If this is possible in the budget and time you have and you have a design(s) that work with that but carry the same style and theme, that would be nice to see but not necessary.
Should not have
• We do not want to put a postal address on the cards

```html
<!DOCTYPE html>
<html lang="en">
<head>
<meta charset="utf-8">
<title>RT Code Transit – Business Card</title>
<link href="https://fonts.googleapis.com/css2?family=Questrial&family=Nunito+Sans:wght@400;600&display=swap" rel="stylesheet">
<style>
  :root {
    --stage: #3a3a3c;
    --blue-deep: #2c45a0;
    --blue-mid: #3b58c4;
    --blue-bright: #4c6fdc;
    --blue-soft: #6f8be6;
    --paper-top: #ffffff;
    --paper-bottom: #d6d7dc;
    --arc-lilac: #c6cdea;
    --arc-grey: #dcdee7;
    --arc-light: #eeeff2;
    --ink: #5a5b60;
    --ink-soft: #6e6f75;
    --white: #ffffff;
  }
  * { margin: 0; padding: 0; box-sizing: border-box; }
  html, body { width: 1200px; height: 900px; overflow: hidden; background: var(--stage); }
  .stage { position: relative; width: 1200px; height: 900px; }
  .card {
    position: absolute; top: 270px; width: 540px; height: 360px;
    border-radius: 26px; overflow: hidden;
  }
  .card__bg { position: absolute; inset: 0; width: 100%; height: 100%; }
  .card--front { left: 40px; background: linear-gradient(180deg, var(--blue-deep) 0%, var(--blue-mid) 45%, var(--blue-bright) 100%); }
  .card--back { left: 620px; background: linear-gradient(180deg, var(--paper-top) 0%, var(--paper-bottom) 100%); }

  .brand { position: absolute; display: flex; align-items: center; gap: 14px; font-family: "Questrial", sans-serif; }
  .brand__dot { border-radius: 50%; flex: none; }
  .brand__name { white-space: nowrap; }

  .card--front .brand { left: 200px; top: 150px; }
  .card--front .brand__dot { width: 46px; height: 46px; background: var(--blue-soft); }
  .card--front .brand__name { font-size: 34px; color: var(--white); }

  .website {
    position: absolute; right: 78px; bottom: 40px;
    font-family: "Nunito Sans", sans-serif; font-size: 14px; font-weight: 600; color: var(--white);
  }

  .card--back .brand { left: 30px; top: 98px; gap: 10px; }
  .card--back .brand__dot { width: 28px; height: 28px; background: var(--blue-bright); }
  .card--back .brand__name { font-size: 26px; color: var(--ink); }

  .person { position: absolute; left: 30px; top: 190px; font-family: "Questrial", sans-serif; }
  .person__name { font-size: 21px; letter-spacing: 0.5px; color: var(--ink); }
  .person__title { font-family: "Nunito Sans", sans-serif; font-size: 15px; color: var(--ink-soft); }

  .contacts {
    position: absolute; left: 30px; top: 250px; list-style: none;
    font-family: "Nunito Sans", sans-serif; font-size: 13.5px; line-height: 17px; color: var(--ink-soft);
  }
  .contacts__label { display: inline-block; width: 18px; }
  .contacts__email { margin-top: 12px; }
</style>
</head>
<body>
<main class="stage">

  <section class="card card--front" aria-label="Card front">
    <svg class="card__bg" viewBox="0 0 540 360" aria-hidden="true">
      <circle cx="520" cy="330" r="240" fill="#ffffff" opacity="0.06"/>
      <circle cx="560" cy="360" r="190" fill="#ffffff" opacity="0.06"/>
    </svg>
    <div class="brand">
      <span class="brand__dot"></span>
      <span class="brand__name">RT Code Transit</span>
    </div>
    <p class="website">www.rtcodetransit.example</p>
  </section>

  <section class="card card--back" aria-label="Card back">
    <svg class="card__bg" viewBox="0 0 540 360" aria-hidden="true">
      <circle cx="530" cy="200" r="250" fill="var(--arc-lilac)" opacity="0.85"/>
      <circle cx="570" cy="270" r="210" fill="var(--arc-grey)"/>
      <circle cx="600" cy="290" r="175" fill="var(--arc-light)"/>
      <path d="M240 360 Q300 320 380 300 L540 300 L540 360 Z" fill="var(--arc-lilac)" opacity="0.5"/>
    </svg>
    <div class="brand">
      <span class="brand__name">RT Code Transit</span>
      <span class="brand__dot"></span>
    </div>
    <div class="person">
      <p class="person__name">MARCUS DELANY</p>
      <p class="person__title">managing director</p>
    </div>
    <ul class="contacts">
      <li><span class="contacts__label">p</span>0207 946 031</li>
      <li><span class="contacts__label">f</span>0207 946 032</li>
      <li><span class="contacts__label">m</span>0770 090 041</li>
      <li class="contacts__email"><span class="contacts__label">e</span>info@rtcodetransit.example</li>
    </ul>
  </section>

</main>
</body>
</html>
```